A Maple Syrup Label for a Local Buniness

We are looking for a label for our maple syrup business. Our business currently sells honey, and we are expanding into maple syrup. Our Business name is "Brackley Honey" and we currently have a logo attached below. We would like to incorporate the bee and BH part, but the label could also read "Brackley Farms" with the words maple syrup. We do not want consumers to confuse the maple syrup jars with the honey jars. It should be clear that the jars contain maple syrup. We are open to new designs as well.

```html
<!DOCTYPE html>
<html lang="en">
<head>
<meta charset="utf-8">
<title>Brackley Farms Maple Syrup Label</title>
<link href="https://fonts.googleapis.com/css2?family=Arimo:wght@400;700&family=Caveat+Brush&display=swap" rel="stylesheet">
<style>
  :root {
    --canvas: #ffffff;
    --label-cream: #fdfbec;
    --label-white: #ffffff;
    --ink: #111111;
    --outline: #3a3a3a;
    --leaf-hot: #f0661f;
    --leaf-warm: #f59a2a;
    --leaf-gold: #f8c13a;
    --gray-dark: #6f6f6f;
    --gray-mid: #9a9a9a;
    --gray-light: #c8c8c8;
    --brand-gold: #e9b512;
  }
  * { margin: 0; padding: 0; box-sizing: border-box; }
  html, body { width: 1200px; height: 675px; overflow: hidden; background: var(--canvas); }
  .canvas {
    width: 1200px; height: 675px;
    display: flex; justify-content: center; align-items: center; gap: 48px;
  }
  .label {
    position: relative;
    width: 265px; height: 428px;
    background: var(--label-cream);
    border: 1px solid var(--outline);
    border-radius: 50% 50% 22% 22% / 42% 42% 8% 8%;
    overflow: hidden;
    font-family: "Arimo", Arial, sans-serif;
    color: var(--ink);
  }
  .label--mono { background: var(--label-white); }

  .brand {
    position: absolute; top: 30px; left: 0; right: 0;
    display: flex; flex-direction: column; align-items: center; gap: 6px;
  }
  .brand__mark {
    width: 22px; height: 22px; border-radius: 50%;
    background: var(--brand-gold);
  }
  .label--mono .brand__mark { background: var(--gray-mid); }
  .brand__name {
    font-size: 14px; font-weight: 700; letter-spacing: 0.5px;
    text-align: center; line-height: 1.05; color: var(--ink);
  }

  .leaf-art {
    position: absolute; top: 104px; left: 0; width: 265px; height: 228px;
    border-radius: 45% 45% 40% 40% / 40% 40% 50% 50%;
    background: radial-gradient(ellipse at 50% 50%, var(--leaf-gold) 0%, var(--leaf-warm) 40%, var(--leaf-hot) 70%, rgba(240,102,31,0) 100%);
  }
  .label--mono .leaf-art {
    background: radial-gradient(ellipse at 50% 50%, var(--gray-light) 0%, var(--gray-mid) 45%, var(--gray-dark) 70%, rgba(111,111,111,0) 100%);
  }

  .product {
    position: absolute; top: 172px; left: 0; right: 0;
  }
  .product__farm {
    display: block; text-align: center;
    font-weight: 700; font-size: 12.5px; line-height: 1.05;
    margin-left: -6px;
  }
  .product__maple, .product__syrup {
    display: block; font-family: "Caveat Brush", cursive;
    font-size: 58px; line-height: 0.9;
  }
  .product__maple { margin-left: 44px; margin-top: 0; }
  .product__syrup { margin-left: 92px; margin-top: -6px; }

  .details {
    position: absolute; right: 36px; top: 344px;
    text-align: right; font-size: 11px; line-height: 1.18;
  }
  .details__weight { font-weight: 700; font-size: 11.5px; margin-bottom: 6px; }
  .details__farm { font-weight: 700; }
</style>
</head>
<body>
<main class="canvas">
  <article class="label label--color">
    <header class="brand">
      <span class="brand__mark"></span>
      <span class="brand__name">BRACKLEY<br>HONEY</span>
    </header>
    <div class="leaf-art" role="img" aria-label="Orange watercolour maple leaf illustration"></div>
    <h1 class="product">
      <span class="product__farm">BRACKLEY<br>FARM’S</span>
      <span class="product__maple">Maple</span>
      <span class="product__syrup">Syrup</span>
    </h1>
    <footer class="details">
      <p class="details__weight">NET WT. 16 OZ</p>
      <p class="details__farm">Brackley Farms</p>
      <p>4410 Ridge Line Road</p>
      <p>Markdale, ON N0C 2H0</p>
    </footer>
  </article>

  <article class="label label--mono">
    <header class="brand">
      <span class="brand__mark"></span>
      <span class="brand__name">BRACKLEY<br>HONEY</span>
    </header>
    <div class="leaf-art" role="img" aria-label="Grey watercolour maple leaf illustration"></div>
    <h1 class="product">
      <span class="product__farm">BRACKLEY<br>FARM’S</span>
      <span class="product__maple">Maple</span>
      <span class="product__syrup">Syrup</span>
    </h1>
    <footer class="details">
      <p class="details__weight">NET WT. 16 OZ</p>
      <p class="details__farm">Brackley Farms</p>
      <p>4410 Ridge Line Road</p>
      <p>Markdale, ON N0C 2H0</p>
    </footer>
  </article>
</main>
</body>
</html>
```